Pebblestone Promotions Flyer Design

I need to be able to have a flyer that shows what I do for businesses. Same logo that you designed.

Requirements
Must have
• I gave an example of what I need it to say in the attachment. Must have logo and resemble business card style.
Nice to have
• It could include pictures of what a digital sign is. We offer an KVRT, weather, and news slide on our advertising. I included sample pictures of those.

```html
<!DOCTYPE html>
<html lang="en">
<head>
<meta charset="utf-8">
<title>Pebblestone Promotions Flyer</title>
<link href="https://fonts.googleapis.com/css2?family=Figtree:wght@400;500;600;700;800&display=swap" rel="stylesheet">
<style>
:root{
  --backdrop:#c3cbb8;
  --paper:#ffffff;
  --green:#8cc63f;
  --charcoal:#5a5a5a;
  --ink:#1f1f1f;
  --screen:#5b5b5b;
  --screen-text:#eef3e4;
}
*{margin:0;padding:0;box-sizing:border-box}
html,body{width:1200px;height:1200px;overflow:hidden}
body{background:var(--backdrop);font-family:"Figtree",Arial,sans-serif;position:relative}
.flyer{position:absolute;left:182px;top:59px;width:836px;height:1082px;background:var(--paper);overflow:hidden}
.brand{position:absolute;left:28px;top:28px;width:420px;font-size:42px;line-height:1.02;font-weight:800;color:var(--charcoal);letter-spacing:-0.5px}
.contact{position:absolute;left:567px;top:20px;width:200px}
.contact h2{font-size:27px;font-weight:700;color:var(--charcoal);padding-bottom:6px;border-bottom:2px solid var(--green);line-height:1.1}
.contact p{display:flex;align-items:center;gap:6px;font-size:15px;color:var(--charcoal);margin-top:7px;line-height:1}
.contact p:first-of-type{margin-top:14px}
.contact svg{width:13px;height:13px;flex:none}
.hero{position:absolute;left:0;top:135px;width:836px;height:490px;
  background:linear-gradient(180deg,#a35a49 0%,#92503f 40%,#5a3a30 70%,#2f2a2d 100%)}
.ad-screen{position:absolute;left:187px;top:157px;width:375px;height:208px;background:var(--screen);border:4px solid #1e1e1e;
  display:flex;align-items:flex-start;justify-content:center;padding-top:14px}
.ad-screen span{font-size:55px;font-weight:700;color:var(--screen-text);line-height:0.98;text-align:center;letter-spacing:-0.5px}
.headline{position:absolute;left:0;top:481px;width:836px;text-align:center;color:#fff;font-size:63px;font-weight:700;line-height:60px;letter-spacing:-0.5px}
.benefits{position:absolute;left:22px;top:638px;width:785px;text-align:center;font-size:41px;font-weight:700;color:var(--green);padding-bottom:8px;border-bottom:2.5px solid var(--green);letter-spacing:-0.3px}
.tab{position:absolute;left:0;top:725px;width:250px;height:45px;background:var(--charcoal);clip-path:polygon(0 0,100% 0,92% 100%,0 100%);
  font-size:26px;font-weight:700;color:var(--green);padding-left:36px;line-height:45px}
.summary{position:absolute;left:279px;top:715px;width:540px;font-size:27px;font-weight:600;color:var(--charcoal);line-height:1.2}
.perks{position:absolute;left:22px;top:792px;width:780px;list-style:none}
.perks li{position:relative;padding-left:14px;font-size:16.2px;line-height:24.6px;color:var(--ink)}
.perks li::before{content:"";position:absolute;left:0;top:8px;width:7px;height:11px;background:var(--green);border-radius:50% 0 50% 0;transform:rotate(25deg)}
.footer-band{position:absolute;left:0;top:1055px;width:836px;height:27px;background:var(--green)}
</style>
</head>
<body>
<main class="flyer">
  <header>
    <div class="brand">Pebblestone Promotions</div>
    <div class="contact">
      <h2>Contact us</h2>
      <p><svg viewBox="0 0 16 16" aria-hidden="true"><path fill="#8cc63f" d="M3.5 1.5l2.5 3-1.5 2c.8 1.8 2.3 3.3 4 4l2-1.5 3 2.5-1.6 2.5C7.5 13.8 2.2 8.5 1 4.1z"/></svg>+555-0142-78</p>
      <p><svg viewBox="0 0 16 16" aria-hidden="true"><rect x="1" y="3" width="14" height="10" fill="#8cc63f"/><path d="M1 3l7 6 7-6" fill="none" stroke="#fff" stroke-width="1.4"/></svg>support@pebblestone.com</p>
    </div>
  </header>

  <section class="hero" role="img" aria-label="Photo of friends cheering at a sports bar with TV screens on a brick wall"></section>
  <div class="ad-screen"><span>YOUR AD<br>HERE</span></div>
  <h1 class="headline">Let us make you famous<br>in your community!</h1>

  <h2 class="benefits">Benefits of Advertising with Pebblestone</h2>
  <div class="tab">WHAT WE DO</div>
  <p class="summary">We design an ad for your company and place it on the TV at local businesses.</p>

  <ul class="perks">
    <li>Inexpensive: Only $31.00 per month!</li>
    <li>Exposure: Our digital signage is placed in only the best/high traffic businesses in your area.</li>
    <li>Repetition: Your ad is shown over 3,500 time each month (42,000 times per year)!</li>
    <li>Local: We show your ad to consumers in YOUR area. Let us help you do business with the people you want to do business with.</li>
    <li>Exclusivity: Only 2 ads per industry.</li>
    <li>Lead Generation: We show consumers how to reach you and where to find you.</li>
    <li>Brand Awareness: People need to know your business. We make that happen by putting your brand right in front of them.</li>
    <li>Digital: Digital advertising has higher retention rates and higher consumer engagement.</li>
  </ul>

  <div class="footer-band"></div>
</main>
</body>
</html>
```